R Hendrow tile

This add will be posted on a shopping cart at grocery store. I have limited space and need something to tie in all my info.Add will be top to bottom not horizontal
R. Hendrow
Custom Tile & Marble
"4 generations of Service"
Our slogan is: creating the most beautiful living spaces
614-283-7150
www.hendrowtile-example.com
email:rkbloom42@mailpost-example.com
in business since 1975
We would like to use the color yellow in the design and R. Hendrow has to be script font to match our trucks.

tile & marble flooring,walls, complete bathroom renovations new homes,remodels,

Shopping

ffc214
000000
b1b1b1
f37123

• Would like yellow to be used sparingly all other colors are just a suggestion. Need R. Hendrow To be in Script all other wording to be straight
• all contact info,other colors to tie into yellow

```html
<!DOCTYPE html>
<html lang="en">
<head>
<meta charset="utf-8">
<title>R. Hendrow Custom Tile &amp; Marble</title>
<link rel="stylesheet" href="https://fonts.googleapis.com/css2?family=Pinyon+Script&family=Raleway:wght@200&family=Arimo:wght@400;700&display=swap">
<style>
  :root {
    --page-bg: #ececec;
    --brand-yellow: #ffc929;
    --ink: #2f2b28;
    --accent-red: #e8452a;
    --slogan-yellow: #ffc214;
    --photo-light: #a58f74;
    --photo-mid: #7d6a55;
    --photo-dark: #3c332b;
  }
  html, body {
    margin: 0;
    width: 1018px;
    height: 1200px;
    overflow: hidden;
    background: var(--page-bg);
  }
  .ad {
    position: absolute;
    left: 182px;
    top: 163px;
    width: 654px;
    height: 845px;
    overflow: hidden;
  }
  .ad__photo {
    position: absolute;
    left: 0; top: 0;
    width: 654px;
    height: 620px;
    background:
      radial-gradient(ellipse at 60% 35%, rgba(0,0,0,0) 0%, rgba(0,0,0,0.25) 90%),
      linear-gradient(180deg, var(--photo-mid) 0%, var(--photo-light) 55%, var(--photo-mid) 100%);
  }
  .ad__slogan {
    position: absolute;
    left: 56px;
    top: 258px;
    margin: 0;
    font-family: "Raleway", "Helvetica Neue", sans-serif;
    font-weight: 200;
    font-size: 78px;
    line-height: 70px;
    letter-spacing: -1px;
    color: var(--slogan-yellow);
  }
  .ad__band {
    position: absolute;
    left: 0; top: 620px;
    width: 654px;
    height: 225px;
    background: var(--brand-yellow);
  }
  .brand {
    position: absolute;
    right: 42px;
    top: 52px;
    text-align: right;
  }
  .brand__name {
    margin: 0;
    font-family: "Pinyon Script", cursive;
    font-size: 62px;
    line-height: 62px;
    color: var(--ink);
  }
  .brand__trade {
    margin: 10px 8px 0 0;
    font-family: "Arimo", Arial, sans-serif;
    font-weight: 700;
    font-size: 16px;
    line-height: 18px;
    color: var(--ink);
  }
  .brand__tagline {
    position: absolute;
    right: 46px;
    top: 161px;
    margin: 0;
    font-family: "Arimo", Arial, sans-serif;
    font-size: 14px;
    color: var(--accent-red);
  }
  .contact {
    position: absolute;
    left: 24px;
    right: 24px;
    top: 202px;
    margin: 0;
    text-align: center;
    font-family: "Arimo", Arial, sans-serif;
    font-size: 11px;
    letter-spacing: -0.1px;
    color: var(--ink);
    white-space: nowrap;
  }
  .contact__sep {
    color: var(--accent-red);
    font-weight: 700;
    padding: 0 2px;
  }
</style>
</head>
<body>
  <main class="ad">
    <div class="ad__photo" role="img" aria-label="Living room with wood-look tile floor, two tall black tufted armchairs, a round glass table and black drum pendant lamps"></div>
    <h1 class="ad__slogan">creating<br>the most<br>beautiful<br>living<br>spaces…</h1>
    <section class="ad__band">
      <div class="brand">
        <p class="brand__name">R. Hendrow</p>
        <p class="brand__trade">CUSTOM TILE &amp; MARBLE</p>
      </div>
      <p class="brand__tagline">“4 GENERATIONS OF SERVICE”</p>
      <p class="contact">614-283-7150<span class="contact__sep">/</span>www.hendrowtile-example.com<span class="contact__sep">/</span>email:rkbloom42@mailpost-example.com<span class="contact__sep">/</span>in business since 1975</p>
    </section>
  </main>
</body>
</html>
```